Website Design For our Tour Company

We need a face lift on our current website. I want it to look the best! Lots of videos. An easy to use website to obtain easy conversions. I want people to feel like they are on the tour just by looking at our website. My current website is just bland and unprofessional looking. I want it to be incredibly mobile friendly and look great on the desk top. Our current website is https://www.kellbrookvoyages.example/
I would like there to be an option where the viewer can select what language they would like to read in. Im hoping you can pull a-lot of media and videos from out facebook page. Im not happy with most of my descriptions for the product and tours we offer. Looking for professional help.

Our two main activities are Summer and Winter Tours
In The Summer the main things we do our Jet Boat & Jet Ski Tours.

In The Winter our main tour is luxury first class Aurora Viewing. I Would like to see a-lot of aurora video/photos as I believe that gets peoples attention!

Target Market(s)

Travelers from china and around the world

Coding

Coded - Design and coding required

Number of Pages Required

5+ page

Requirements
Must have
• be able to select what when language you would like to read the website in.
Nice to have
• The overall look and feel I want for the website is luxury, fancy, royalty. Think Gerald Mossworth. I like the Luxury gold colors. I need the website to look ridiculously professional

incorporate Lots of Aurora photos / videos as one of our main tours is Aurora

```html
<!DOCTYPE html>
<html lang="en">
<head>
<meta charset="utf-8">
<title>Kellbrook Voyages</title>
<link href="https://fonts.googleapis.com/css2?family=Montserrat:wght@400;500;600;700&family=Open+Sans:wght@400;600&display=swap" rel="stylesheet">
<style>
:root{
  --gold:#b39869;
  --gold-dark:#9c8256;
  --ink:#1d1d1d;
  --text:#555;
  --muted:#8a8a8a;
  --light:#f2f2f2;
  --black:#0c0c0c;
  --white:#fff;
}
*{box-sizing:border-box;margin:0;padding:0}
html,body{width:1200px;height:4780px;overflow:hidden}
body{font-family:"Open Sans",Arial,sans-serif;color:var(--text);background:var(--white);position:relative}
h1,h2,h3,h4,.btn,.nav,.logo-name{font-family:"Montserrat",Arial,sans-serif}
.btn{display:inline-block;background:var(--gold);color:var(--white);font-size:15px;font-weight:600;letter-spacing:1px;text-transform:uppercase;padding:16px 34px;border-radius:2px}
.section-title{font-size:48px;font-weight:700;color:var(--ink);text-align:center;text-transform:uppercase;letter-spacing:1px}

/* hero */
.hero{position:relative;height:610px;background:linear-gradient(180deg,#0a1423 0%,#15324a 30%,#2d6b58 55%,#1a2f2a 75%,#0c1512 100%);overflow:hidden}
.hero-photo{position:absolute;inset:0;background:radial-gradient(ellipse 60% 40% at 55% 45%,rgba(90,220,140,.55),transparent 70%),radial-gradient(ellipse 40% 25% at 30% 30%,rgba(160,90,200,.35),transparent 70%)}
.header{position:absolute;top:0;left:0;right:0;height:84px;display:flex;align-items:center;padding:0 100px 0 110px;background:rgba(0,0,0,.35)}
.logo{display:flex;align-items:center;gap:12px}
.logo-mark{width:36px;height:36px;border-radius:50%;background:var(--gold)}
.logo-name{font-size:24px;font-weight:600;color:var(--white);letter-spacing:1px}
.nav{display:flex;gap:26px;margin-left:56px;margin-top:34px;font-size:15px;font-weight:500;color:var(--white)}
.nav .active{color:var(--gold)}
.header-right{position:absolute;right:100px;top:14px;display:flex;align-items:center;gap:18px;font-family:"Montserrat",Arial,sans-serif;font-size:14px;font-weight:600;color:var(--white)}
.book{border:1px solid var(--white);padding:8px 14px}
.hero-title{position:absolute;top:185px;width:100%;text-align:center;font-size:64px;line-height:1.12;font-weight:600;color:var(--white);letter-spacing:2px}
.hero-btn{position:absolute;top:372px;left:50%;transform:translateX(-50%);background:var(--white);color:var(--ink);font-family:"Montserrat",Arial,sans-serif;font-weight:600;font-size:16px;padding:18px 34px;white-space:nowrap}
.arrow{position:absolute;top:285px;width:30px;height:30px}

/* intro */
.intro{height:990px;padding-top:72px;text-align:center}
.intro h2{font-size:44px;line-height:1.2;font-weight:700;color:var(--ink);text-transform:uppercase}
.intro p{width:780px;margin:34px auto 0;font-size:16px;line-height:1.75}
.intro .btn{margin-top:38px}
.season-row{display:flex;gap:22px;justify-content:center;margin-top:58px}
.season{width:478px}
.season-photo{height:368px}
.season h3{margin-top:34px;font-size:28px;font-weight:700;color:var(--ink);text-transform:uppercase}
.season span{display:block;margin-top:8px;font-size:16px;color:var(--ink)}

/* packages */
.packages{height:900px;background:var(--light);padding-top:38px}
.card-grid{display:grid;grid-template-columns:repeat(3,316px);gap:28px 12px;justify-content:center;margin-top:40px}
.card{background:var(--white);height:280px;box-shadow:0 1px 3px rgba(0,0,0,.08)}
.card-photo{height:212px}
.card-info{padding:10px 14px;display:flex;justify-content:space-between;font-size:13px}
.card-info h4{font-size:18px;font-weight:600;color:var(--ink);margin-top:6px}
.price{color:var(--gold);font-family:"Montserrat",Arial,sans-serif;font-weight:700;font-size:18px;align-self:flex-end}
.packages .btn,.gallery .btn{display:block;width:max-content;margin:60px auto 0}

/* gallery */
.gallery{height:828px;padding-top:56px}
.gallery-row{display:flex;gap:12px;justify-content:center;margin-top:40px}
.gallery-row+.gallery-row{margin-top:16px}
.g3{width:316px;height:252px}
.g2{width:478px;height:252px}
.gallery .btn{margin-top:48px}

/* testimonials */
.testimonials{position:relative;height:452px;background:linear-gradient(180deg,#2e3440 0%,#4a4f5c 55%,#3b2f2c 100%);text-align:center;color:var(--white);padding-top:46px}
.testimonials h2{color:var(--white)}
.testimonials blockquote{width:760px;margin:28px auto 0;font-style:italic;font-size:15px;line-height:1.7}
.avatar{width:64px;height:64px;border-radius:50%;background:#b7b7b7;margin:22px auto 0}
.testimonials cite{display:block;margin-top:14px;font-style:normal;font-family:"Montserrat",Arial,sans-serif;font-size:17px}

/* videos */
.videos{position:relative;height:360px;padding-top:40px}
.video-row{display:flex;gap:22px;justify-content:center;margin-top:34px}
.video{position:relative;width:310px;height:208px}
.play{position:absolute;left:50%;top:50%;transform:translate(-50%,-50%)}

/* subscribe */
.subscribe{display:flex;height:260px}
.subscribe-photo{width:600px}
.subscribe-box{flex:1;background:var(--gold);padding:36px 48px;color:var(--white)}
.subscribe-box h2{font-size:44px;font-weight:700;letter-spacing:1px}
.subscribe-box p{margin-top:8px;font-size:16px}
.form{display:flex;margin-top:30px}
.form .field{width:380px;height:52px;background:var(--white);color:var(--muted);font-size:14px;padding:16px}
.form .go{width:54px;height:52px;background:var(--black);display:flex;align-items:center;justify-content:center}

/* footer */
.footer{height:380px;background:var(--black);color:#d5d5d5;padding:60px 110px 0}
.footer-cols{display:flex}
.footer-about{width:430px}
.footer-about p{margin-top:26px;font-size:15px;line-height:1.7}
.footer-links{margin-left:120px;list-style:none;font-size:15px;line-height:2}
.footer-contact{margin-left:90px;font-family:"Montserrat",Arial,sans-serif;font-size:15px;font-weight:600}
.social{width:36px;height:36px;border:1px solid #d5d5d5;border-radius:50%;margin-top:22px}
.copyright{border-top:1px solid #2c2c2c;margin-top:38px;padding-top:20px;text-align:center;font-size:14px}
</style>
</head>
<body>

<section class="hero">
  <div class="hero-photo" role="img" aria-label="Green aurora over a forest lake at night"></div>
  <header class="header">
    <div class="logo"><span class="logo-mark"></span><span class="logo-name">Kellbrook Voyages</span></div>
    <nav class="nav">
      <span class="active">Home</span><span>Summer Tours</span><span>Winter Tours</span><span>Car Rentals</span><span>Blog</span><span>Contact</span>
    </nav>
    <div class="header-right">
      <span>
        <svg width="14" height="14" viewBox="0 0 24 24" fill="#fff"><path d="M6.6 10.8a15.1 15.1 0 0 0 6.6 6.6l2.2-2.2a1 1 0 0 1 1-.25 11.4 11.4 0 0 0 3.6.57 1 1 0 0 1 1 1V20a1 1 0 0 1-1 1A17 17 0 0 1 3 4a1 1 0 0 1 1-1h3.5a1 1 0 0 1 1 1c0 1.25.2 2.450.57 3.57a1 1 0 0 1-.25 1z"/></svg>
        CALL/TEXT - 907-555-0148</span>
      <span class="book">BOOK ONLINE</span>
      <span>ENG ▾</span>
    </div>
  </header>
  <svg class="arrow" style="left:10px" viewBox="0 0 30 30"><path d="M19 6 10 15l9 9" stroke="#fff" stroke-width="3" fill="none"/></svg>
  <svg class="arrow" style="right:10px" viewBox="0 0 30 30"><path d="m11 6 9 9-9 9" stroke="#fff" stroke-width="3" fill="none"/></svg>
  <h1 class="hero-title">TAKING YOU WHERE<br>YOU WANT TO GO</h1>
  <span class="hero-btn">BEGIN ADVENTURE</span>
</section>

<section class="intro">
  <h2>Take your next trip with<br>Kellbrook Resorts, LLC</h2>
  <p>Kellbrook Resorts, LLC specializes in providing the best travel services in Fairbanks, Alaska. We've been in Fairbanks since 1995, creating customized itineraries for our clients based around their personal plans and preferences. In our line of work we don't only make plans, we help you build experiences and memories. Let us arrange the details of your next trip — call today for a free consultation.</p>
  <span class="btn">About Us</span>
  <div class="season-row">
    <div class="season">
      <div class="season-photo" role="img" aria-label="Guests on a jet ski on a summer river" style="background:linear-gradient(180deg,#7fa4b8,#3f6f7a 60%,#c9a640)"></div>
      <h3>Summer Tours</h3><span>Land Of The Midnight Sun</span>
    </div>
    <div class="season">
      <div class="season-photo" role="img" aria-label="Guests in winter gear on snow" style="background:linear-gradient(180deg,#c9d2dc,#e9eef2 55%,#a03a3a)"></div>
      <h3>Winter Tours</h3><span>Explore The Winter Wonderland</span>
    </div>
  </div>
</section>

<section class="packages">
  <h2 class="section-title">Most Popular Packages</h2>
  <div class="card-grid">
    <div class="card"><div class="card-photo" role="img" aria-label="Jet boat on an icy river" style="background:linear-gradient(180deg,#5d8fc4,#a9c7e2 60%,#f1f4f7)"></div>
      <div class="card-info"><div><span>◷ 3 Hours</span><h4>Jet Boat Adventure</h4></div><span class="price">$145</span></div></div>
    <div class="card"><div class="card-photo" role="img" aria-label="Snowshoers in a snowy forest" style="background:linear-gradient(180deg,#cdd8e2,#eef2f5 60%,#6d7b86)"></div>
      <div class="card-info"><div><span>◷ December - April</span><h4>Alaska Snowshoe</h4></div><span class="price">$65</span></div></div>
    <div class="card"><div class="card-photo" role="img" aria-label="Jet boat on open water" style="background:linear-gradient(180deg,#3f87c9,#9cc6e6 55%,#365d74)"></div>
      <div class="card-info"><div><span>◷ 1 Hour</span><h4>Jet Boat</h4></div><span class="price">$95</span></div></div>
    <div class="card"><div class="card-photo" role="img" aria-label="Green aurora over snowy trees" style="background:linear-gradient(180deg,#0e2230,#1f8a62 55%,#0f1f1c)"></div>
      <div class="card-info"><div><span>◷ 3 Hours</span><h4>Incredible Aurora</h4></div><span class="price">$145</span></div></div>
    <div class="card"><div class="card-photo" role="img" aria-label="Dog sled team on a snowy trail" style="background:linear-gradient(180deg,#b9a28a,#e8e4de 60%,#6b5d50)"></div>
      <div class="card-info"><div><span>◷ December - March</span><h4>Thrilling Sledding</h4></div><span class="price">$85</span></div></div>
    <div class="card"><div class="card-photo" role="img" aria-label="Ice fishing catch in winter" style="background:linear-gradient(180deg,#9aa3ac,#6b4a3c 60%,#d6d9dc)"></div>
      <div class="card-info"><div><span>◷ December - April</span><h4>Alaska Ice Fishing</h4></div><span class="price">$95</span></div></div>
  </div>
  <span class="btn">Explore More</span>
</section>

<section class="gallery">
  <h2 class="section-title">Our Gallery</h2>
  <div class="gallery-row">
    <div class="g3" role="img" aria-label="Off-road vehicle by a lake at dusk" style="background:linear-gradient(180deg,#8aa9c4,#c08a5a 60%,#3c3a2e)"></div>
    <div class="g3" role="img" aria-label="Sunset through bare winter trees" style="background:linear-gradient(180deg,#f0c27a,#d98a4a 50%,#e6e3de)"></div>
    <div class="g3" role="img" aria-label="Kayaker on a calm river" style="background:linear-gradient(180deg,#6b8a5a,#3f5f6a 60%,#b84a30)"></div>
  </div>
  <div class="gallery-row">
    <div class="g2" role="img" aria-label="Jet ski on a lake at sunset" style="background:linear-gradient(180deg,#4c5e80,#b88e8a 50%,#2a3040)"></div>
    <div class="g2" role="img" aria-label="Kayak on a forest lake" style="background:linear-gradient(180deg,#7fb3d8,#3f7a4a 50%,#4f7f8f)"></div>
  </div>
  <span class="btn">View More</span>
</section>

<section class="testimonials" role="img" aria-label="Winter landscape at twilight behind the testimonials">
  <svg class="arrow" style="left:40px;top:210px" viewBox="0 0 30 30"><path d="M19 6 10 15l9 9" stroke="#fff" stroke-width="3" fill="none"/></svg>
  <svg class="arrow" style="right:40px;top:210px" viewBox="0 0 30 30"><path d="m11 6 9 9-9 9" stroke="#fff" stroke-width="3" fill="none"/></svg>
  <h2 class="section-title">Client Testimonials</h2>
  <blockquote>“ Every moment of the trip felt planned just for us. The guides were warm, the aurora was unforgettable and the lodge felt like a private retreat. We are already planning our next winter visit with the team. ”</blockquote>
  <div class="avatar"></div>
  <cite>John Doe</cite>
</section>

<section class="videos">
  <h2 class="section-title">Videos</h2>
  <svg class="arrow" style="left:60px;top:230px" viewBox="0 0 30 30"><path d="M19 6 10 15l9 9" stroke="#999" stroke-width="3" fill="none"/></svg>
  <svg class="arrow" style="right:60px;top:230px" viewBox="0 0 30 30"><path d="m11 6 9 9-9 9" stroke="#999" stroke-width="3" fill="none"/></svg>
  <div class="video-row">
    <div class="video" role="img" aria-label="Video: jet boats on a river" style="background:linear-gradient(180deg,#7a8a6a,#4a5a4a 60%,#8a5a3a)">
      <svg class="play" width="54" height="54" viewBox="0 0 54 54"><circle cx="27" cy="27" r="27" fill="rgba(0,0,0,.6)"/><path d="M22 17v20l16-10z" fill="#fff"/></svg></div>
    <div class="video" role="img" aria-label="Video: lake at sunset" style="background:linear-gradient(180deg,#cfd6e0,#8aa0b8 55%,#1e2a34)">
      <svg class="play" width="54" height="54" viewBox="0 0 54 54"><circle cx="27" cy="27" r="27" fill="rgba(0,0,0,.6)"/><path d="M22 17v20l16-10z" fill="#fff"/></svg></div>
    <div class="video" role="img" aria-label="Video: jet ski ride on a lake" style="background:linear-gradient(180deg,#8aa6c8,#5a6a8a 50%,#b84040)">
      <svg class="play" width="54" height="54" viewBox="0 0 54 54"><circle cx="27" cy="27" r="27" fill="rgba(0,0,0,.6)"/><path d="M22 17v20l16-10z" fill="#fff"/></svg></div>
  </div>
</section>

<section class="subscribe">
  <div class="subscribe-photo" role="img" aria-label="Pink sunset over a still lake" style="background:linear-gradient(180deg,#3a4a7a,#d98aa0 45%,#5a4a6a 60%,#1a1a2a)"></div>
  <div class="subscribe-box">
    <h2>SUBSCRIBE</h2>
    <p>To receive promotions and newsletter</p>
    <div class="form">
      <span class="field">Email Address</span>
      <span class="go"><svg width="20" height="16" viewBox="0 0 20 16"><path d="M0 8h17M11 2l6 6-6 6" stroke="#fff" stroke-width="2.4" fill="none"/></svg></span>
    </div>
  </div>
</section>

<footer class="footer">
  <div class="footer-cols">
    <div class="footer-about">
      <div class="logo"><span class="logo-mark"></span><span class="logo-name">Kellbrook Voyages</span></div>
      <p>Kellbrook Resorts, LLC specializes in providing the best travel services in Fairbanks, Alaska. We've been in Fairbanks since 1995, creating customized itineraries for our clients based around their personal plans and preferences.</p>
    </div>
    <ul class="footer-links">
      <li>Home</li><li>Summer Tours</li><li>Winter Tours</li><li>Car Rentals</li><li>Blog</li><li>Contact</li>
    </ul>
    <div class="footer-contact">
      <div>CALL/TEXT - 907-555-0148</div>
      <div class="social"></div>
    </div>
  </div>
  <div class="copyright">Kellbrook Voyages © 2020</div>
</footer>

</body>
</html>
```